Modern Design Business Card industrial maintenance company

Business card design for Company named Brookvale Equipment Services

Target Market(s)

Industrial

Industry/Entity Type

Maintenance and repair

Contact Information for Business Card

Place holder for address, office phone, mobile number and email

Requirements
Must have
• Clean modern look
Nice to have
• N/a

```html
<!DOCTYPE html>
<html lang="en">
<head>
<meta charset="utf-8">
<title>Brookvale Equipment Services – Business Card</title>
<link href="https://fonts.googleapis.com/css2?family=Lato:wght@400;700&display=swap" rel="stylesheet">
<style>
  :root {
    --page-bg: #e9e6e1;
    --card-dark: #141414;
    --card-dark-edge: #262626;
    --panel-frost: #9a958e;
    --champagne: #d8c3a6;
    --champagne-soft: #c9b79f;
    --seal-fill: #e4d5c0;
    --seal-ink: #161616;
  }
  html, body {
    margin: 0;
    width: 1200px;
    height: 1047px;
    overflow: hidden;
    background: var(--page-bg);
    font-family: "Lato", Arial, sans-serif;
  }
  .card {
    position: absolute;
    left: 100px;
    top: 252px;
    width: 1000px;
    height: 543px;
    border-radius: 26px;
    overflow: hidden;
    background: var(--panel-frost);
    box-shadow: 0 18px 40px rgba(0,0,0,0.18);
  }
  .card__front {
    position: absolute;
    left: 0; top: 0;
    width: 725px;
    height: 100%;
    background: linear-gradient(100deg, var(--card-dark) 0%, var(--card-dark-edge) 55%, var(--card-dark) 100%);
  }
  .company-name {
    position: absolute;
    left: 62px;
    top: 58px;
    margin: 0;
    width: 520px;
    font-weight: 700;
    font-size: 30px;
    letter-spacing: 4px;
    line-height: 1.15;
    color: var(--champagne);
    text-transform: uppercase;
  }
  .person {
    position: absolute;
    left: 62px;
    top: 218px;
    color: var(--champagne);
  }
  .person__name {
    margin: 0;
    font-weight: 700;
    font-size: 40px;
    letter-spacing: 1px;
  }
  .person__role {
    margin: 4px 0 0;
    font-size: 24px;
    color: var(--champagne-soft);
  }
  .address {
    position: absolute;
    left: 58px;
    top: 326px;
    margin: 0;
    font-style: normal;
    font-size: 24px;
    line-height: 32px;
    color: var(--champagne-soft);
  }
  .contacts {
    position: absolute;
    left: 58px;
    top: 412px;
    margin: 0;
    padding: 0;
    list-style: none;
    font-size: 24px;
    color: var(--champagne-soft);
  }
  .contacts li {
    display: flex;
    align-items: center;
    height: 38px;
  }
  .contacts svg {
    width: 22px;
    height: 22px;
    margin-right: 26px;
    fill: none;
    stroke: var(--champagne-soft);
    stroke-width: 1.8;
  }
  .seal {
    position: absolute;
    left: 504px;
    top: 52px;
    width: 436px;
    height: 436px;
    border-radius: 50%;
    background: var(--seal-fill);
    display: flex;
    align-items: center;
    justify-content: center;
  }
  .seal__name {
    font-weight: 700;
    font-size: 40px;
    letter-spacing: 3px;
    color: var(--seal-ink);
    text-transform: uppercase;
  }
</style>
</head>
<body>
  <section class="card" aria-label="Brookvale Equipment Services business card">
    <div class="card__front">
      <h1 class="company-name">Brookvale<br>Equipment Services</h1>

      <div class="person">
        <p class="person__name">DANIEL REYES</p>
        <p class="person__role">Founder &amp; CEO</p>
      </div>

      <address class="address">
        1234 First Line Address<br>
        5678 Second Line Address
      </address>

      <ul class="contacts">
        <li>
          <svg viewBox="0 0 24 24" aria-hidden="true"><path d="M5 3h4l2 5-3 2a12 12 0 0 0 6 6l2-3 5 2v4a2 2 0 0 1-2 2A18 18 0 0 1 3 5a2 2 0 0 1 2-2z"/></svg>
          222-4444-8888
        </li>
        <li>
          <svg viewBox="0 0 24 24" aria-hidden="true"><rect x="2" y="5" width="20" height="14" rx="1"/><path d="M2 6l10 7 10-7"/></svg>
          info@yourmail.com
        </li>
        <li>
          <svg viewBox="0 0 24 24" aria-hidden="true"><circle cx="12" cy="12" r="10"/><path d="M2 12h20M12 2c3 3 3 17 0 20M12 2c-3 3-3 17 0 20"/></svg>
          www.yourwebsite.com
        </li>
      </ul>
    </div>

    <div class="seal">
      <span class="seal__name">Brookvale</span>
    </div>
  </section>
</body>
</html>
```